Business Card Design

Harbourline Recruitment is a specialist financial services recruitment company and implementation partner

Industry/Entity Type

Business

Contact Information for Business Card

Tom Ashford
Harbourline Recruitment Ltd
e:tom.ashford@harbourline-staffing.com
m:07834 206 148
m:07712 438 560
s: tommashford

```html
<!DOCTYPE html>
<html lang="en">
<head>
<meta charset="utf-8">
<title>Harbourline Recruitment – Business Card</title>
<link rel="stylesheet" href="https://fonts.googleapis.com/css2?family=Montserrat:wght@300;400;700&display=swap">
<style>
  :root {
    --page-bg: #ececea;
    --card-front: #000000;
    --card-back: #858585;
    --ink-light: #ffffff;
    --rule: #d6d6d6;
  }
  * { box-sizing: border-box; margin: 0; padding: 0; }
  html, body {
    width: 1200px;
    height: 857px;
    overflow: hidden;
    background: var(--page-bg);
    font-family: "Montserrat", Arial, sans-serif;
  }
  .card-set {
    position: absolute;
    inset: 0;
    display: flex;
    align-items: center;
    justify-content: center;
    gap: 40px;
  }
  .card {
    position: relative;
    width: 540px;
    height: 309px;
    border-radius: 36px;
    box-shadow: 0 10px 24px rgba(0, 0, 0, 0.18);
    color: var(--ink-light);
  }
  /* Front */
  .card-front {
    background: var(--card-front);
    display: flex;
    flex-direction: column;
    align-items: center;
    justify-content: center;
    gap: 34px;
  }
  .brand {
    display: flex;
    align-items: center;
    gap: 14px;
  }
  .brand-mark {
    width: 22px;
    height: 22px;
    border: 2px solid var(--ink-light);
  }
  .brand-name {
    font-weight: 400;
    font-size: 20px;
    letter-spacing: 0.06em;
    text-transform: uppercase;
  }
  .holder-name {
    font-weight: 700;
    font-size: 22px;
    letter-spacing: 0.04em;
    text-transform: uppercase;
  }
  /* Back */
  .card-back {
    background: var(--card-back);
    display: flex;
    align-items: center;
    padding-left: 70px;
  }
  .back-mark {
    width: 78px;
    height: 78px;
    background: var(--ink-light);
    flex-shrink: 0;
  }
  .back-rule {
    width: 2px;
    height: 150px;
    background: var(--rule);
    margin: 0 22px 0 36px;
  }
  .contact-list {
    list-style: none;
    font-weight: 300;
    font-size: 14px;
    line-height: 1.75;
  }
  .contact-list .phone { font-weight: 400; font-size: 15px; }
</style>
</head>
<body>
  <main class="card-set">
    <section class="card card-front" aria-label="Business card front">
      <div class="brand">
        <span class="brand-mark"></span>
        <span class="brand-name">Harbourline Recruitment Ltd</span>
      </div>
      <p class="holder-name">Tom Ashford</p>
    </section>

    <section class="card card-back" aria-label="Business card back">
      <span class="back-mark"></span>
      <span class="back-rule"></span>
      <ul class="contact-list">
        <li>e:tom.ashford@harbourline-staffing.com</li>
        <li class="phone">m:07834 206 148</li>
        <li class="phone">m:07712 438 560</li>
        <li>s: tommashford</li>
      </ul>
    </section>
  </main>
</body>
</html>
```